依頼詳細
展示会の会場を歩いているお客様に一目でこの商品がどのようなものかを理解していただけるような、わかりやすく、目を引くインパクトのあるデザインを希望します。
記載項目
商品名(点検口の安全金網 Rフレア)/社名/キャッチコピー/ロゴ
詳細は添付ファイル参照
サイズ
B1(縦横どちらも可)
ページ数
片面
希望イメージ
シンプル 複雑
単色 カラフル
暗い 明るい
日常 高級
遊び心 厳粛
未来的 伝統的
女性的 男性的
希望する色
オレンジ(黄色めの)と黒 その他の色も可
納品ファイル
• 高解像度JPG (.jpg)
• イラストレーター形式 (.ai)
補足説明
Rフレア http://item.sorabazaar.jp/lumo-shop/c/0000000830/
点検口 http://item.sorabazaar.jp/lumo-shop/c/0000000480/

```html
<!DOCTYPE html>
<html lang="ja">
<head>
<meta charset="utf-8">
<title>点検口の安全金網 Rフレア</title>
<link rel="stylesheet" href="https://fonts.googleapis.com/css2?family=Dela+Gothic+One&family=Noto+Sans+JP:wght@700;900&display=swap">
<style>
  :root {
    --ink: #0d0d0d;
    --steel-dark: #1a1c1f;
    --steel-mid: #3a3d42;
    --warning: #ffe100;
    --alert-red: #d8101c;
    --white: #ffffff;
    --product-red: #b9472e;
    --product-steel: #9ea3a8;
  }
  html, body {
    margin: 0;
    padding: 0;
    width: 846px;
    height: 1200px;
    overflow: hidden;
    background: var(--ink);
  }
  .poster {
    position: relative;
    width: 846px;
    height: 1200px;
    overflow: hidden;
    font-family: "Noto Sans JP", sans-serif;
    color: var(--white);
  }
  .machinery-backdrop {
    position: absolute;
    inset: 0;
    background:
      radial-gradient(ellipse at 80% 20%, rgba(110,115,122,0.55), transparent 55%),
      radial-gradient(ellipse at 15% 55%, rgba(80,84,90,0.45), transparent 50%),
      linear-gradient(170deg, var(--steel-mid) 0%, var(--steel-dark) 45%, var(--ink) 80%);
  }
  .hand-photo {
    position: absolute;
    left: 230px;
    top: 15px;
    width: 290px;
    height: 140px;
    border-radius: 40px 60px 30px 50px;
    background: linear-gradient(160deg, #f1d2bd, #c99a7f);
  }
  .lead {
    position: absolute;
    left: 118px;
    top: 185px;
    margin: 0;
    writing-mode: vertical-rl;
    font-weight: 900;
    font-size: 31px;
    line-height: 1.5;
    letter-spacing: 1px;
  }
  .product-photo {
    position: absolute;
    left: 225px;
    top: 320px;
    width: 380px;
    height: 620px;
    border-radius: 36px;
    background:
      radial-gradient(ellipse at 50% 65%, var(--product-steel), transparent 55%),
      linear-gradient(180deg, #c7643f 0%, var(--product-red) 60%, #7e2e1d 100%);
  }
  .headline {
    position: absolute;
    right: 28px;
    top: 14px;
    margin: 0;
    z-index: 2;
    writing-mode: vertical-rl;
    font-family: "Dela Gothic One", sans-serif;
    font-weight: 400;
    font-size: 205px;
    line-height: 1;
    letter-spacing: -12px;
    color: var(--warning);
  }
  .features {
    position: absolute;
    left: 24px;
    top: 500px;
    margin: 0;
    padding: 0;
    list-style: none;
  }
  .feature {
    width: 84px;
    height: 84px;
    margin-bottom: 12px;
    border-radius: 50%;
    background: var(--alert-red);
    display: flex;
    align-items: center;
    justify-content: center;
    text-align: center;
    font-weight: 900;
    font-size: 15px;
    line-height: 1.25;
  }
  .benefit {
    position: absolute;
    left: 0;
    right: 0;
    top: 968px;
    margin: 0;
    text-align: center;
    font-weight: 900;
    font-size: 44px;
    line-height: 1.2;
    letter-spacing: 3px;
  }
  .mini-photo {
    position: absolute;
    left: 14px;
    top: 1036px;
    width: 212px;
    height: 138px;
    border-radius: 16px;
    background: linear-gradient(160deg, #d4d7da, #6d7176);
  }
  .brand-plate {
    position: absolute;
    left: 240px;
    top: 1058px;
    width: 566px;
    height: 82px;
    border-radius: 12px;
    background: var(--warning);
    color: var(--ink);
    display: flex;
    align-items: center;
    padding: 0 22px;
    box-sizing: border-box;
    gap: 16px;
  }
  .brand-plate__tag {
    font-weight: 900;
    font-size: 22px;
    line-height: 1.2;
  }
  .brand-plate__mark {
    width: 46px;
    height: 46px;
    background: var(--ink);
    flex: none;
  }
  .brand-plate__name {
    font-weight: 900;
    font-size: 60px;
    line-height: 1;
    letter-spacing: 2px;
  }
  .company {
    position: absolute;
    right: 40px;
    top: 1150px;
    margin: 0;
    font-weight: 700;
    font-size: 20px;
    line-height: 1.2;
  }
</style>
</head>
<body>
<main class="poster">
  <div class="machinery-backdrop" role="img" aria-label="暗い背景に並ぶ歯車とスパナなどの機械部品"></div>
  <div class="hand-photo" role="img" aria-label="点検口へ伸びる作業者の手"></div>

  <p class="lead">現場の作業者を<br>機械の巻込まれ事故から守る!</p>

  <div class="product-photo" role="img" aria-label="蓋の開いた赤い点検口に取り付けた安全金網"></div>

  <h1 class="headline">危ない!</h1>

  <ul class="features">
    <li class="feature">溶接不要</li>
    <li class="feature">3分で<br>取付け<br>取外し</li>
    <li class="feature">しかも<br>ローコスト</li>
  </ul>

  <p class="benefit">工具の落下や手足の侵入を防止</p>

  <div class="mini-photo" role="img" aria-label="安全金網単体の製品写真"></div>

  <div class="brand-plate">
    <span class="brand-plate__tag">点検口の<br>安全金網</span>
    <span class="brand-plate__mark"></span>
    <span class="brand-plate__name">Rフレア</span>
  </div>

  <p class="company">株式会社ミナトテック</p>
</main>
</body>
</html>
```